Brightvale Crew Word Press Website

We need a graphical, fun website that conveys our messaging of providing the Best-In-Class Signature Marketing System for Mortgage Loan Officers and Realtors. Our system uses AI and Predictive Analysis to uncover the 'Gold' hidden in contact databases. The 'Gold' is defined as people who are in the market or likely to be in the market soon. We place that 'Gold' in the form of Contact Name, Address, Phone and Email on a Daily To Do List detailing what type of contact should be made.

Target Market(s)

Mortgage Loan Officers and Realtors

Industry/Entity Type

Mortgage & Real Estate

Coding

Coded - Design and coding required

Number of Pages Required

5+ page

Requirements
Must have
• I like the look of this site- https://www.homeloanpromostudio.example/
Nice to have
• Please create a flow that is similar to https://www.homeloanpromostudio.example/, but better, more dynamic. Site must be responsive and mobile friendly. Site will have embedded videos. Site need to convey a message of hope, imagination, innovation, results oriented, better than the rest, victory!
Should not have
• Nothing cheesy or low class.

```html
<!DOCTYPE html>
<html lang="en">
<head>
<meta charset="utf-8">
<title>Brightvale Crew – Website Layout Board</title>
<link href="https://fonts.googleapis.com/css2?family=Poppins:wght@400;500;600;700&display=swap" rel="stylesheet">
<style>
:root{
  --blue:#1a8fd0;
  --blue-deep:#0d6ca8;
  --blue-light:#1fa6e0;
  --blue-bar:#0a5f96;
  --gold:#e9b52c;
  --gold-light:#f4c93c;
  --ink:#1c1c2a;
  --body:#4a4a55;
  --mist:#f1f2f6;
  --white:#ffffff;
}
*{margin:0;padding:0;box-sizing:border-box}
html,body{width:1200px;height:2846px;overflow:hidden}
body{position:relative;background:var(--white);font-family:'Poppins',sans-serif;color:var(--ink)}
.abs{position:absolute}
.board-bg{position:absolute;left:0;top:0}
.board-title{position:absolute;top:58px;font-size:47px;font-weight:600;color:var(--blue);letter-spacing:.5px}
.board-title span{color:var(--gold-light)}
.board-title.desktop{left:314px}
.board-title.mobile{left:848px}

.frame{position:absolute;overflow:hidden;background:var(--white);box-shadow:0 4px 18px rgba(0,0,0,.12)}
.band{position:absolute;left:0;width:100%}
.band.hero,.band.features,.band.footer{background:linear-gradient(135deg,var(--blue-deep) 0%,var(--blue) 45%,var(--blue-light) 100%)}
.band.mist{background:var(--mist)}
.band.bar{background:var(--blue-bar)}
.btn{position:absolute;display:flex;align-items:center;justify-content:center;background:linear-gradient(180deg,var(--gold-light),var(--gold));color:var(--white);font-weight:600;letter-spacing:2px;border-radius:2px}
.center{text-align:center}
.white{color:var(--white)}
.brand{position:absolute;display:flex;align-items:center;gap:6px;font-weight:700;color:var(--gold-light);white-space:nowrap}
.brand .dot{display:inline-block;border-radius:50%;background:var(--gold-light)}
.photo{position:absolute}
.more{position:absolute;font-weight:600;color:var(--gold);letter-spacing:1.5px;border-bottom:1px solid var(--gold);padding-bottom:1px}
.h-section{position:absolute;font-weight:700;color:var(--ink);white-space:nowrap}
.para{position:absolute;color:var(--body)}
.tick{position:absolute}
.check-text{position:absolute;font-weight:500;color:var(--ink)}
.ci{position:absolute;border-radius:50%;background:var(--gold-light);display:flex;align-items:center;justify-content:center}
.social{position:absolute;border-radius:50%;background:var(--gold-light)}
.arrow{position:absolute;border-radius:50%;display:flex;align-items:center;justify-content:center}

.desk{left:104px;top:138px;width:731px;height:2307px}
.desk .topbar{position:absolute;left:427px;top:0;width:304px;height:19px;background:var(--gold);color:var(--white);font-size:7.5px;display:flex;align-items:center;gap:14px;padding-left:22px;clip-path:polygon(6% 0,100% 0,100% 100%,0 100%)}
.desk .nav{position:absolute;top:34px;font-size:9.5px;color:var(--white);font-weight:500}
.desk .nav-dot{position:absolute;left:384px;top:50px;width:3px;height:3px;border-radius:50%;background:var(--gold-light)}
.desk .hero-sub{position:absolute;left:0;width:731px;top:108px;font-size:13.5px;font-weight:600}
.desk .hero-title{position:absolute;left:0;width:731px;top:126px;font-size:32px;line-height:38px;font-weight:700}
.desk .scroll{position:absolute;left:0;width:731px;top:315px;font-size:6.5px;letter-spacing:1.5px}
.desk .svc-icon{position:absolute;top:822px;width:58px;height:58px;border-radius:7px;display:flex;align-items:center;justify-content:center}
.desk .svc-name{position:absolute;top:889px;width:130px;font-size:9.5px;font-weight:600}
.desk .svc-desc{position:absolute;top:906px;width:130px;font-size:8.8px;line-height:14px;color:var(--body)}
.desk .feat{position:absolute;font-size:9.5px;font-weight:600;color:var(--white)}
.desk .blog-date{position:absolute;top:1897px;font-size:6.5px;color:var(--blue)}
.desk .blog-title{position:absolute;top:1907px;font-size:10px;font-weight:600}
.desk .blog-desc{position:absolute;top:1925px;width:165px;font-size:8.3px;line-height:13.5px;color:var(--body)}
.desk .foot-text{position:absolute;font-size:8.8px;line-height:14px;color:var(--white)}

.mob{left:918px;top:138px;width:184px;height:2660px}
.mob .fi{position:absolute;left:65px;font-size:9px;font-weight:600;color:var(--white)}
.mob .foot-text{position:absolute;left:45px;font-size:8.5px;line-height:13px;color:var(--white)}
</style>
</head>
<body>

<svg class="board-bg" width="1200" height="2846" viewBox="0 0 1200 2846" aria-hidden="true">
  <polygon points="1200,22 1200,2846 392,2846" fill="#deaf3a"/>
</svg>

<div class="board-title desktop">Desktop <span>View</span></div>
<div class="board-title mobile">Mobile <span>View</span></div>

<!-- ================= DESKTOP ================= -->
<div class="frame desk">

  <section class="band hero" style="top:0;height:410px"></section>
  <div class="topbar">
    <span>&#9742; 01 555 0142 88</span><span>&#9993; info@brightvalecrew.example</span>
  </div>
  <div class="brand" style="left:100px;top:44px;font-size:13px"><span class="dot" style="width:9px;height:9px"></span>Brightvale Crew</div>
  <div class="nav" style="left:372px">Home</div>
  <div class="nav-dot"></div>
  <div class="nav" style="left:425px">Services</div>
  <div class="nav" style="left:489px">About</div>
  <div class="nav" style="left:543px">Blog</div>
  <div class="nav" style="left:588px">Contact</div>
  <div class="hero-sub center white">Best-In-Class Signature Marketing System for</div>
  <h1 class="hero-title center white">Mortgage Loan Officers<br>and Realtors</h1>
  <div class="btn" style="left:313px;top:216px;width:105px;height:25px;font-size:7.5px">KNOW MORE</div>
  <svg class="abs" style="left:357px;top:282px" width="17" height="26" viewBox="0 0 17 26" aria-hidden="true">
    <rect x="1" y="1" width="15" height="24" rx="7.5" fill="none" stroke="#fff" stroke-width="1.4"/>
    <line x1="8.5" y1="6" x2="8.5" y2="10" stroke="#fff" stroke-width="1.4" stroke-linecap="round"/>
  </svg>
  <div class="scroll center white">SCROLLDOWN</div>
  <svg class="abs" style="left:0;top:326px" width="731" height="90" viewBox="0 0 731 90" aria-hidden="true">
    <path d="M0,88 Q330,-10 731,78 L731,90 L0,90 Z" fill="#fff"/>
    <path d="M0,80 Q330,-22 731,74" fill="none" stroke="#f0c02e" stroke-width="3.5"/>
  </svg>

  <!-- about -->
  <div class="photo" role="img" aria-label="Laptop and phone showing the marketing dashboard" style="left:350px;top:415px;width:325px;height:290px;border-radius:14px;background:linear-gradient(160deg,#f4f2f0 0%,#e3dedb 55%,#d7cfd0 100%)"></div>
  <div class="abs" style="left:106px;top:420px;font-size:19px">About</div>
  <h2 class="h-section" style="left:106px;top:448px;font-size:26px">Brightvale Crew</h2>
  <p class="para" style="left:106px;top:494px;width:225px;font-size:9.3px;line-height:16.5px">Lorem ipsum dolor sit amet, consetur adipiscing elit. Integer suscipit in leo in semper. Nunc sed metus malesuada, rutrum erat non, eleifend est. Aenean sit amet viverra metus, sed tincidunt leo. Fusce pretium nunc risus, et sodales quam tincidunt porta.</p>
  <div class="btn" style="left:104px;top:610px;width:105px;height:25px;font-size:7.5px">READ MORE</div>

  <!-- services -->
  <section class="band mist" style="top:724px;height:306px"></section>
  <h2 class="h-section center" style="left:0;width:731px;top:752px;font-size:31px">Our Services</h2>

  <div class="svc-icon" style="left:135px;background:#c9eefb">
    <svg width="32" height="26" viewBox="0 0 32 26" aria-hidden="true"><rect x="1" y="1" width="20" height="14" rx="3" fill="#2aa6e0"/><rect x="11" y="9" width="20" height="14" rx="3" fill="#7fd0f2"/><rect x="5" y="5" width="12" height="6" rx="1" fill="#fff"/></svg>
  </div>
  <div class="svc-name center" style="left:99px">Mortgage Chatbot</div>
  <div class="svc-desc center" style="left:99px">Maecenas arcu ri posuere ac lacus vitae</div>
  <div class="more" style="left:136px;top:942px;font-size:7.5px">READ MORE</div>

  <div class="svc-icon" style="left:269px;background:#fde0cc">
    <svg width="26" height="26" viewBox="0 0 26 26" aria-hidden="true"><circle cx="13" cy="8" r="6" fill="#f09a55"/><path d="M2,25 Q13,10 24,25 Z" fill="#f09a55"/></svg>
  </div>
  <div class="svc-name center" style="left:233px">Reputation Management</div>
  <div class="svc-desc center" style="left:233px">Maecenas arcu ri posuere ac lacus vitae</div>
  <div class="more" style="left:270px;top:942px;font-size:7.5px">READ MORE</div>

  <div class="svc-icon" style="left:404px;background:#fbd3e5">
    <svg width="28" height="24" viewBox="0 0 28 24" aria-hidden="true"><polygon points="3,8 12,8 24,2 24,22 12,16 3,16" fill="#e8468d"/><rect x="6" y="16" width="4" height="6" fill="#e8468d"/></svg>
  </div>
  <div class="svc-name center" style="left:368px">Marketing</div>
  <div class="svc-desc center" style="left:368px">Maecenas arcu ri posuere ac lacus vitae</div>
  <div class="more" style="left:405px;top:942px;font-size:7.5px">READ MORE</div>

  <div class="svc-icon" style="left:540px;background:#dcf2d2">
    <svg width="28" height="26" viewBox="0 0 28 26" aria-hidden="true"><rect x="3" y="14" width="5" height="10" fill="#5fb548"/><rect x="11" y="8" width="5" height="16" fill="#5fb548"/><rect x="19" y="3" width="5" height="21" fill="#5fb548"/></svg>
  </div>
  <div class="svc-name center" style="left:504px">Realtors</div>
  <div class="svc-desc center" style="left:504px">Maecenas arcu ri posuere ac lacus vitae</div>
  <div class="more" style="left:541px;top:942px;font-size:7.5px">READ MORE</div>

  <div class="btn" style="left:325px;top:980px;width:82px;height:25px;font-size:7.5px">VIEW ALL</div>

  <!-- gold features -->
  <section class="band features" style="top:1030px;height:370px"></section>
  <div class="photo" role="img" aria-label="Phone showing two professionals reviewing work together" style="left:156px;top:1045px;width:128px;height:268px;border-radius:14px;border:3px solid #e9eef2;background:linear-gradient(170deg,#d9d4cd 0%,#a89788 45%,#3b3d48 100%)"></div>
  <h2 class="abs white" style="left:360px;top:1060px;font-size:30px;line-height:33px;font-weight:700">Our Gold<br>Features</h2>
  <p class="para" style="left:360px;top:1135px;width:255px;font-size:8.8px;line-height:14.5px;color:#fff">Lorem ipsum dolor sit amet, consetur ading elit. Integer suscipit in leo in semper. Nunc sed metus malesuada, rutrum erat non, eleifend est. tincidunt porta.</p>

  <svg class="abs" style="left:358px;top:1190px" width="26" height="26" viewBox="0 0 26 26" aria-hidden="true"><rect x="5" y="2" width="16" height="22" rx="2" fill="none" stroke="#fff" stroke-width="1.3"/><line x1="9" y1="9" x2="17" y2="9" stroke="#fff" stroke-width="1.3"/><line x1="9" y1="14" x2="17" y2="14" stroke="#fff" stroke-width="1.3"/><line x1="9" y1="19" x2="14" y2="19" stroke="#fff" stroke-width="1.3"/></svg>
  <div class="feat" style="left:394px;top:1197px">Aenean sollicitudin</div>
  <svg class="abs" style="left:504px;top:1188px" width="22" height="30" viewBox="0 0 22 30" aria-hidden="true"><rect x="3" y="2" width="16" height="26" rx="2" fill="none" stroke="#fff" stroke-width="1.3"/><rect x="6" y="5" width="10" height="6" fill="none" stroke="#fff" stroke-width="1.1"/><circle cx="8" cy="16" r="1" fill="#fff"/><circle cx="14" cy="16" r="1" fill="#fff"/><circle cx="8" cy="22" r="1" fill="#fff"/><circle cx="14" cy="22" r="1" fill="#fff"/></svg>
  <div class="feat" style="left:538px;top:1197px">Aenean sollicitudin</div>
  <svg class="abs" style="left:356px;top:1236px" width="30" height="26" viewBox="0 0 30 26" aria-hidden="true"><ellipse cx="10" cy="20" rx="8" ry="3" fill="none" stroke="#fff" stroke-width="1.3"/><ellipse cx="10" cy="15" rx="8" ry="3" fill="none" stroke="#fff" stroke-width="1.3"/><circle cx="21" cy="9" r="7" fill="none" stroke="#fff" stroke-width="1.3"/></svg>
  <div class="feat" style="left:394px;top:1245px">Fusce vulputate</div>
  <svg class="abs" style="left:504px;top:1236px" width="28" height="26" viewBox="0 0 28 26" aria-hidden="true"><circle cx="16" cy="7" r="5" fill="none" stroke="#fff" stroke-width="1.3"/><path d="M2,16 L9,16 L15,19 L24,16 L26,18 L15,24 L2,22" fill="none" stroke="#fff" stroke-width="1.3"/></svg>
  <div class="feat" style="left:538px;top:1245px">Vivamus fermentum</div>

  <svg class="abs" style="left:0;top:1320px" width="731" height="82" viewBox="0 0 731 82" aria-hidden="true">
    <path d="M0,80 Q330,-18 731,60 L731,82 L0,82 Z" fill="#fff"/>
    <path d="M0,74 Q330,-30 731,56" fill="none" stroke="#f0c02e" stroke-width="3.5"/>
  </svg>

  <!-- recent work -->
  <h2 class="h-section" style="left:104px;top:1425px;font-size:30px">Recent Work</h2>
  <p class="para" style="left:106px;top:1469px;width:210px;font-size:8.8px;line-height:14.5px">Vestibulum sit amet enim quis est maximus laoreet eu ut nisl. Ut at orci porta, sollicitudin tortor vitae, vehicula nulla.</p>
  <svg class="tick" style="left:104px;top:1525px" width="10" height="8" viewBox="0 0 10 8" aria-hidden="true"><path d="M1,4 L4,7 L9,1" fill="none" stroke="#5cb85c" stroke-width="1.6"/></svg>
  <div class="check-text" style="left:117px;top:1523px;width:210px;font-size:8.5px;line-height:14px">Vivamus fermentum a leo ut accumsan.</div>
  <svg class="tick" style="left:104px;top:1547px" width="10" height="8" viewBox="0 0 10 8" aria-hidden="true"><path d="M1,4 L4,7 L9,1" fill="none" stroke="#5cb85c" stroke-width="1.6"/></svg>
  <div class="check-text" style="left:117px;top:1544px;width:200px;font-size:8.5px;line-height:14px">Duis vitae neque ut libero imperdiet fringilla vel nec mauris.</div>
  <svg class="tick" style="left:104px;top:1581px" width="10" height="8" viewBox="0 0 10 8" aria-hidden="true"><path d="M1,4 L4,7 L9,1" fill="none" stroke="#5cb85c" stroke-width="1.6"/></svg>
  <div class="check-text" style="left:117px;top:1578px;width:210px;font-size:8.5px;line-height:14px">Quisque mattis nibh sit amet turpis hendrerit, quis vulputate magna ultricies.</div>
  <div class="btn" style="left:106px;top:1622px;width:110px;height:25px;font-size:7.5px">VIEW PROJCET</div>
  <div class="abs" style="left:352px;top:1424px;width:313px;height:208px;border-radius:8px 8px 0 0;background:#d9dde2;padding:6px 6px 0">
    <div class="photo" role="img" aria-label="Team meeting in a bright office" style="position:relative;width:100%;height:100%;background:linear-gradient(120deg,#eef1f3 0%,#c9cfd5 40%,#6b7078 75%,#3a3f47 100%)"></div>
  </div>
  <div class="abs" style="left:314px;top:1632px;width:389px;height:10px;border-radius:0 0 12px 12px;background:linear-gradient(180deg,#c7ccd2,#8c9198)"></div>

  <!-- latest blog -->
  <section class="band mist" style="top:1702px;height:330px"></section>
  <h2 class="h-section center" style="left:0;width:731px;top:1715px;font-size:30px">Latest Blog</h2>
  <div class="photo" role="img" aria-label="Two colleagues working at a laptop" style="left:104px;top:1777px;width:164px;height:112px;background:linear-gradient(135deg,#e8e4de,#a9a39c 60%,#5c5a58)"></div>
  <div class="photo" role="img" aria-label="Team discussing notes at a wall" style="left:284px;top:1777px;width:165px;height:112px;background:linear-gradient(135deg,#f1ece6,#c9b9a6 50%,#7b6f62)"></div>
  <div class="photo" role="img" aria-label="Business meeting around a table" style="left:463px;top:1777px;width:164px;height:112px;background:linear-gradient(135deg,#eef2f4,#bfc8cf 55%,#63707b)"></div>
  <div class="arrow" style="left:93px;top:1826px;width:22px;height:22px;background:rgba(120,120,130,.55)"><svg width="8" height="10" viewBox="0 0 8 10" aria-hidden="true"><path d="M6,1 L2,5 L6,9" fill="none" stroke="#fff" stroke-width="1.5"/></svg></div>
  <div class="arrow" style="left:617px;top:1826px;width:22px;height:22px;background:var(--blue-light)"><svg width="8" height="10" viewBox="0 0 8 10" aria-hidden="true"><path d="M2,1 L6,5 L2,9" fill="none" stroke="#fff" stroke-width="1.5"/></svg></div>

  <div class="blog-date" style="left:104px">Feb 18, 2022</div>
  <div class="blog-title" style="left:104px">Integer vel magna at purus</div>
  <p class="blog-desc" style="left:104px">Aliquam diam libero, ultrices sed neque vel, auctor orn mauris. Integer pellentesque bibendum purus,</p>
  <div class="more" style="left:104px;top:1975px;font-size:7.5px">READ MORE</div>

  <div class="blog-date" style="left:284px">Feb 18, 2022</div>
  <div class="blog-title" style="left:284px">Integer vel magna at purus</div>
  <p class="blog-desc" style="left:284px">Aliquam diam libero, ultrices sed neque vel, auctor orn mauris. Integer pellentesque bibendum purus,</p>
  <div class="more" style="left:284px;top:1975px;font-size:7.5px">READ MORE</div>

  <div class="blog-date" style="left:463px">Feb 18, 2022</div>
  <div class="blog-title" style="left:463px">Integer vel magna at purus</div>
  <p class="blog-desc" style="left:463px">Aliquam diam libero, ultrices sed neque vel, auctor orn mauris. Integer pellentesque bibendum purus,</p>
  <div class="more" style="left:463px;top:1975px;font-size:7.5px">READ MORE</div>

  <!-- footer -->
  <section class="band footer" style="top:2012px;height:259px"></section>
  <svg class="abs" style="left:0;top:2000px" width="731" height="84" viewBox="0 0 731 84" aria-hidden="true">
    <path d="M0,0 L731,0 L731,18 Q380,110 0,18 Z" fill="#fff"/>
    <path d="M0,0 L731,0 L731,4 Q380,92 0,4 Z" fill="#f1f2f6"/>
    <path d="M0,5 Q380,94 731,5" fill="none" stroke="#f0c02e" stroke-width="3.5"/>
  </svg>

  <div class="ci" style="left:116px;top:2127px;width:26px;height:26px"><svg width="10" height="13" viewBox="0 0 10 13" aria-hidden="true"><path d="M5,12 C1,7 1,5 1,4.5 A4,4 0 0 1 9,4.5 C9,5 9,7 5,12 Z" fill="#fff"/><circle cx="5" cy="4.5" r="1.5" fill="#e9b52c"/></svg></div>
  <div class="foot-text" style="left:148px;top:2126px;width:140px">27 Marlow Street,<br>Sydney, Australia</div>
  <div class="ci" style="left:116px;top:2170px;width:26px;height:26px"><svg width="12" height="9" viewBox="0 0 12 9" aria-hidden="true"><rect x="0.5" y="0.5" width="11" height="8" fill="#fff"/><path d="M0.5,0.5 L6,5 L11.5,0.5" fill="none" stroke="#e9b52c" stroke-width="1"/></svg></div>
  <div class="foot-text" style="left:148px;top:2176px">info@brightvalecrew.example</div>
  <div class="ci" style="left:116px;top:2217px;width:26px;height:26px"><svg width="11" height="11" viewBox="0 0 11 11" aria-hidden="true"><path d="M2,0.5 L4,3 L3,4.5 Q4.5,7 6.5,8 L8,7 L10.5,9 L9,10.5 Q3,10 0.5,2 Z" fill="#fff"/></svg></div>
  <div class="foot-text" style="left:148px;top:2223px">01 555 0142 88</div>

  <div class="brand" style="left:308px;top:2178px;font-size:13px;gap:5px"><span class="dot" style="width:8px;height:8px"></span>Brightvale Crew</div>

  <div class="abs white" style="left:464px;top:2112px;font-size:14.5px;line-height:16px;font-weight:600">Subscribe For Latest<br>Update</div>
  <div class="abs" style="left:464px;top:2156px;width:162px;height:24px;background:#fff;font-size:7px;color:#9a9aa5;display:flex;align-items:center;padding-left:8px">&#9993;&nbsp; Enter email address</div>
  <div class="btn" style="left:464px;top:2188px;width:162px;height:24px;font-size:7.5px">SUBSCRIBE</div>

  <section class="band bar" style="top:2271px;height:36px"></section>
  <div class="abs white" style="left:106px;top:2284px;font-size:7.5px">© 2022 <span style="color:var(--gold-light)">Brightvale Crew</span>. All right reserved</div>
  <div class="social" style="left:562px;top:2279px;width:18px;height:18px"></div>
  <div class="social" style="left:585px;top:2279px;width:18px;height:18px"></div>
  <div class="social" style="left:608px;top:2279px;width:18px;height:18px"></div>
</div>

<!-- ================= MOBILE ================= -->
<div class="frame mob">
  <section class="band hero" style="top:0;height:227px"></section>
  <div class="brand" style="left:9px;top:32px;font-size:9px;gap:4px"><span class="dot" style="width:6px;height:6px"></span>Brightvale Crew</div>
  <svg class="abs" style="left:159px;top:8px" width="15" height="12" viewBox="0 0 15 12" aria-hidden="true"><rect y="0" width="15" height="2" fill="#fff"/><rect y="5" width="15" height="2" fill="#fff"/><rect y="10" width="15" height="2" fill="#fff"/></svg>
  <div class="abs center white" style="left:0;width:184px;top:64px;font-size:9px;line-height:14px;font-weight:600">Best-In-Class Signature<br>Marketing System for</div>
  <div class="abs center white" style="left:0;width:184px;top:93px;font-size:12.5px;line-height:18px;font-weight:700">Mortgage Loan Officers<br>and Realtors</div>
  <div class="btn" style="left:50px;top:140px;width:84px;height:20px;font-size:6px">KNOW MORE</div>

  <div class="abs center" style="left:0;width:184px;top:256px;font-size:13px">About</div>
  <h2 class="h-section center" style="left:0;width:184px;top:272px;font-size:18px">Brightvale Crew</h2>
  <p class="para center" style="left:10px;width:164px;top:303px;font-size:8px;line-height:14px">Lorem ipsum dolor sit et, consetur adipiscing elit. Integer suscipit in leo in semper.</p>
  <div class="btn" style="left:45px;top:370px;width:94px;height:25px;font-size:7.5px">READ MORE</div>
  <div class="photo" role="img" aria-label="Laptop and phone showing the marketing dashboard" style="left:13px;top:411px;width:157px;height:130px;border-radius:10px;background:linear-gradient(160deg,#f4f2f0 0%,#e3dedb 55%,#d7cfd0 100%)"></div>

  <section class="band mist" style="top:560px;height:236px"></section>
  <h2 class="h-section center" style="left:0;width:184px;top:583px;font-size:18px">Our Services</h2>
  <div class="abs" style="left:61px;top:633px;width:62px;height:61px;border-radius:7px;background:#c9eefb;display:flex;align-items:center;justify-content:center">
    <svg width="32" height="26" viewBox="0 0 32 26" aria-hidden="true"><rect x="1" y="1" width="20" height="14" rx="3" fill="#2aa6e0"/><rect x="11" y="9" width="20" height="14" rx="3" fill="#7fd0f2"/><rect x="5" y="5" width="12" height="6" rx="1" fill="#fff"/></svg>
  </div>
  <div class="arrow" style="left:11px;top:657px;width:14px;height:14px;background:rgba(120,120,130,.5)"><svg width="6" height="8" viewBox="0 0 6 8" aria-hidden="true"><path d="M5,1 L2,4 L5,7" fill="none" stroke="#fff" stroke-width="1.3"/></svg></div>
  <div class="arrow" style="left:159px;top:657px;width:14px;height:14px;background:var(--blue-light)"><svg width="6" height="8" viewBox="0 0 6 8" aria-hidden="true"><path d="M1,1 L4,4 L1,7" fill="none" stroke="#fff" stroke-width="1.3"/></svg></div>
  <div class="abs center" style="left:0;width:184px;top:703px;font-size:9px;font-weight:600">Mortgage Chatbot</div>
  <div class="abs center" style="left:30px;width:124px;top:720px;font-size:8px;line-height:14px;color:var(--body)">Maecenas arcu ri posuere ac lacus vitae</div>
  <div class="more" style="left:62px;top:755px;font-size:7px">READ MORE</div>

  <section class="band features" style="top:796px;height:646px"></section>
  <div class="photo" role="img" aria-label="Phone showing two professionals reviewing work together" style="left:30px;top:831px;width:125px;height:265px;border-radius:12px;border:3px solid #e9eef2;background:linear-gradient(170deg,#d9d4cd 0%,#a89788 45%,#3b3d48 100%)"></div>
  <h2 class="abs center white" style="left:0;width:184px;top:1106px;font-size:20px;line-height:28px;font-weight:700">Our Gold<br>Features</h2>
  <p class="para center" style="left:12px;width:160px;top:1170px;font-size:8px;line-height:14.5px;color:#fff">Lorem ipsum dolor sit amet, consetur adipiscing elit. Integer suscipit in leo in semper.</p>

  <svg class="abs" style="left:28px;top:1237px" width="26" height="26" viewBox="0 0 26 26" aria-hidden="true"><rect x="5" y="2" width="16" height="22" rx="2" fill="none" stroke="#fff" stroke-width="1.3"/><line x1="9" y1="9" x2="17" y2="9" stroke="#fff" stroke-width="1.3"/><line x1="9" y1="14" x2="17" y2="14" stroke="#fff" stroke-width="1.3"/><line x1="9" y1="19" x2="14" y2="19" stroke="#fff" stroke-width="1.3"/></svg>
  <div class="fi" style="top:1244px">Aenean sollicitudin</div>
  <svg class="abs" style="left:30px;top:1286px" width="22" height="30" viewBox="0 0 22 30" aria-hidden="true"><rect x="3" y="2" width="16" height="26" rx="2" fill="none" stroke="#fff" stroke-width="1.3"/><rect x="6" y="5" width="10" height="6" fill="none" stroke="#fff" stroke-width="1.1"/><circle cx="8" cy="16" r="1" fill="#fff"/><circle cx="14" cy="16" r="1" fill="#fff"/><circle cx="8" cy="22" r="1" fill="#fff"/><circle cx="14" cy="22" r="1" fill="#fff"/></svg>
  <div class="fi" style="top:1295px">Aenean sollicitudin</div>
  <svg class="abs" style="left:26px;top:1339px" width="30" height="26" viewBox="0 0 30 26" aria-hidden="true"><ellipse cx="10" cy="20" rx="8" ry="3" fill="none" stroke="#fff" stroke-width="1.3"/><ellipse cx="10" cy="15" rx="8" ry="3" fill="none" stroke="#fff" stroke-width="1.3"/><circle cx="21" cy="9" r="7" fill="none" stroke="#fff" stroke-width="1.3"/></svg>
  <div class="fi" style="top:1346px">Fusce vulputate</div>
  <svg class="abs" style="left:26px;top:1382px" width="28" height="26" viewBox="0 0 28 26" aria-hidden="true"><circle cx="16" cy="7" r="5" fill="none" stroke="#fff" stroke-width="1.3"/><path d="M2,16 L9,16 L15,19 L24,16 L26,18 L15,24 L2,22" fill="none" stroke="#fff" stroke-width="1.3"/></svg>
  <div class="fi" style="top:1389px">Vivamus fermentum</div>

  <h2 class="h-section center" style="left:0;width:184px;top:1467px;font-size:18px">Recent Work</h2>
  <p class="para center" style="left:12px;width:160px;top:1500px;font-size:8px;line-height:14.5px">Vestibulum sit amet enim quis est maximus laoreet eu ut nisl. Ut at orci porta, sollicitudin tortor vitae, vehicula nulla.</p>
  <svg class="tick" style="left:11px;top:1570px" width="9" height="7" viewBox="0 0 10 8" aria-hidden="true"><path d="M1,4 L4,7 L9,1" fill="none" stroke="#5cb85c" stroke-width="1.6"/></svg>
  <div class="check-text" style="left:25px;top:1566px;width:150px;font-size:8px;line-height:13.5px">Vivamus fermentum a leo ut accumsan.</div>
  <svg class="tick" style="left:11px;top:1607px" width="9" height="7" viewBox="0 0 10 8" aria-hidden="true"><path d="M1,4 L4,7 L9,1" fill="none" stroke="#5cb85c" stroke-width="1.6"/></svg>
  <div class="check-text" style="left:25px;top:1603px;width:140px;font-size:8px;line-height:13.5px">Duis vitae neque ut libero imperdiet fringilla vel nec mauris.</div>
  <svg class="tick" style="left:11px;top:1657px" width="9" height="7" viewBox="0 0 10 8" aria-hidden="true"><path d="M1,4 L4,7 L9,1" fill="none" stroke="#5cb85c" stroke-width="1.6"/></svg>
  <div class="check-text" style="left:25px;top:1653px;width:150px;font-size:8px;line-height:13.5px">Quisque mattis nibh sit amet turpis hendrerit, quis vulputate magna ultricies.</div>
  <div class="btn" style="left:40px;top:1708px;width:104px;height:27px;font-size:7.5px">VIEW PROJECT</div>
  <div class="abs" style="left:16px;top:1757px;width:152px;height:98px;border-radius:5px 5px 0 0;background:#d9dde2;padding:3px 3px 0">
    <div class="photo" role="img" aria-label="Team meeting in a bright office" style="position:relative;width:100%;height:100%;background:linear-gradient(120deg,#eef1f3 0%,#c9cfd5 40%,#6b7078 75%,#3a3f47 100%)"></div>
  </div>
  <div class="abs" style="left:0;top:1855px;width:184px;height:6px;border-radius:0 0 8px 8px;background:linear-gradient(180deg,#c7ccd2,#8c9198)"></div>

  <section class="band mist" style="top:1895px;height:304px"></section>
  <h2 class="h-section center" style="left:0;width:184px;top:1913px;font-size:18px">Latest Blog</h2>
  <div class="photo" role="img" aria-label="Two colleagues working at a laptop" style="left:10px;top:1953px;width:161px;height:110px;background:linear-gradient(135deg,#e8e4de,#a9a39c 60%,#5c5a58)"></div>
  <div class="arrow" style="left:3px;top:2004px;width:16px;height:16px;background:rgba(120,120,130,.55)"><svg width="6" height="8" viewBox="0 0 6 8" aria-hidden="true"><path d="M5,1 L2,4 L5,7" fill="none" stroke="#fff" stroke-width="1.3"/></svg></div>
  <div class="arrow" style="left:163px;top:2004px;width:16px;height:16px;background:var(--blue-light)"><svg width="6" height="8" viewBox="0 0 6 8" aria-hidden="true"><path d="M1,1 L4,4 L1,7" fill="none" stroke="#fff" stroke-width="1.3"/></svg></div>
  <div class="abs" style="left:10px;top:2071px;font-size:6.5px;color:var(--blue)">Feb 18, 2022</div>
  <div class="abs" style="left:10px;top:2080px;font-size:9.5px;font-weight:600">Integer vel magna at purus</div>
  <p class="abs" style="left:10px;top:2097px;width:165px;font-size:7.8px;line-height:13px;color:var(--body)">Aliquam diam libero, ultrices sed neque vel, auctor orn mauris. Integer pellentesque bibendum purus,</p>
  <div class="more" style="left:10px;top:2149px;font-size:7px">READ MORE</div>

  <section class="band footer" style="top:2199px;height:437px"></section>
  <div class="brand" style="left:36px;top:2266px;font-size:14px;gap:5px"><span class="dot" style="width:8px;height:8px"></span>Brightvale Crew</div>

  <div class="ci" style="left:11px;top:2347px;width:26px;height:26px"><svg width="10" height="13" viewBox="0 0 10 13" aria-hidden="true"><path d="M5,12 C1,7 1,5 1,4.5 A4,4 0 0 1 9,4.5 C9,5 9,7 5,12 Z" fill="#fff"/><circle cx="5" cy="4.5" r="1.5" fill="#e9b52c"/></svg></div>
  <div class="foot-text" style="top:2347px">27 Marlow Street,<br>Sydney, Australia</div>
  <div class="ci" style="left:11px;top:2395px;width:26px;height:26px"><svg width="12" height="9" viewBox="0 0 12 9" aria-hidden="true"><rect x="0.5" y="0.5" width="11" height="8" fill="#fff"/><path d="M0.5,0.5 L6,5 L11.5,0.5" fill="none" stroke="#e9b52c" stroke-width="1"/></svg></div>
  <div class="foot-text" style="top:2402px;font-size:8px">info@brightvalecrew.example</div>
  <div class="ci" style="left:11px;top:2441px;width:26px;height:26px"><svg width="11" height="11" viewBox="0 0 11 11" aria-hidden="true"><path d="M2,0.5 L4,3 L3,4.5 Q4.5,7 6.5,8 L8,7 L10.5,9 L9,10.5 Q3,10 0.5,2 Z" fill="#fff"/></svg></div>
  <div class="foot-text" style="top:2448px">01 555 0142 88</div>

  <div class="abs white" style="left:10px;top:2495px;font-size:10px;font-weight:600">Subscribe For Latest Update</div>
  <div class="abs" style="left:10px;top:2518px;width:163px;height:25px;background:#fff;font-size:7px;color:#9a9aa5;display:flex;align-items:center;padding-left:7px">&#9993;&nbsp; Enter email address</div>
  <div class="btn" style="left:10px;top:2552px;width:163px;height:25px;font-size:7.5px">SUBSCRIBE</div>
  <div class="social" style="left:61px;top:2598px;width:17px;height:17px"></div>
  <div class="social" style="left:84px;top:2598px;width:17px;height:17px"></div>
  <div class="social" style="left:106px;top:2598px;width:17px;height:17px"></div>

  <section class="band bar" style="top:2636px;height:24px"></section>
  <div class="abs center white" style="left:0;width:184px;top:2643px;font-size:6px">© 2022 <span style="color:var(--gold-light)">Brightvale Crew</span>. All right reserved</div>
</div>

<div class="brand" style="left:133px;top:2640px;font-size:26px;gap:10px;color:var(--blue)"><span class="dot" style="width:18px;height:18px;background:var(--gold-light)"></span>Brightvale Crew</div>

</body>
</html>
```